Business Card Design

Company is a Commercial Building Company specialising in New Construction and existing refurbishments

Business

Contact Information for Business Card

Derek Halloway
Construction Manager
E Derek@ridgemarkbuilding.com.au
M 0400 215 397
Mail 14 Tarrington Loop Halden Bay WA 6209

```html
<!DOCTYPE html>
<html lang="en">
<head>
<meta charset="utf-8">
<title>Ridgemark Building &amp; Construction – Business Card</title>
<link rel="stylesheet" href="https://fonts.googleapis.com/css2?family=Questrial&display=swap">
<style>
  :root {
    --backdrop: #ecedeb;
    --navy: #1b2757;
    --navy-deep: #141d45;
    --paper: #ffffff;
    --teal: #4fd8cf;
    --orange: #f28a1e;
    --ink: #3a3d44;
    --white: #ffffff;
  }
  * { margin: 0; padding: 0; box-sizing: border-box; }
  html, body {
    width: 1200px;
    height: 857px;
    overflow: hidden;
    background: var(--backdrop);
    font-family: "Questrial", sans-serif;
  }
  .sheet {
    position: relative;
    width: 1200px;
    height: 857px;
    display: flex;
    align-items: center;
    justify-content: center;
    gap: 60px;
  }
  .card {
    width: 500px;
    height: 306px;
    border-radius: 30px;
    position: relative;
    box-shadow: 0 6px 18px rgba(0, 0, 0, 0.12);
    overflow: hidden;
  }
  /* Front */
  .card-front {
    background: linear-gradient(160deg, var(--navy) 0%, var(--navy-deep) 100%);
    display: flex;
    align-items: center;
    justify-content: center;
  }
  .brand {
    display: flex;
    align-items: center;
    gap: 16px;
  }
  .brand-square {
    width: 34px;
    height: 34px;
    background: var(--teal);
  }
  .brand-name {
    color: var(--white);
    font-size: 22px;
    line-height: 1.15;
    letter-spacing: 0.02em;
    text-transform: uppercase;
  }
  /* Back */
  .card-back {
    background: var(--paper);
    display: flex;
    align-items: center;
    justify-content: center;
    gap: 18px;
  }
  .person {
    text-align: right;
    color: var(--orange);
    align-self: flex-start;
    margin-top: 112px;
  }
  .person-name {
    font-size: 15px;
    font-weight: 700;
    letter-spacing: 0.03em;
    text-transform: uppercase;
  }
  .person-role {
    font-size: 13px;
    margin-top: 3px;
  }
  .contact-list {
    list-style: none;
    color: var(--ink);
    font-size: 13px;
    line-height: 1.35;
    align-self: flex-start;
    margin-top: 108px;
  }
  .contact-item {
    display: flex;
    align-items: flex-start;
    gap: 7px;
  }
  .contact-icon {
    flex: none;
    width: 11px;
    height: 11px;
    margin-top: 3px;
  }
</style>
</head>
<body>
  <main class="sheet">
    <section class="card card-front" aria-label="Card front">
      <div class="brand">
        <span class="brand-square"></span>
        <p class="brand-name">Ridgemark Building<br>&amp; Construction</p>
      </div>
    </section>

    <section class="card card-back" aria-label="Card back">
      <div class="person">
        <p class="person-name">Derek Halloway</p>
        <p class="person-role">Construction Manager</p>
      </div>
      <ul class="contact-list">
        <li class="contact-item">
          <svg class="contact-icon" viewBox="0 0 12 12" aria-hidden="true">
            <circle cx="6" cy="6" r="6" fill="#4fd8cf"/>
            <rect x="3" y="4" width="6" height="4.2" fill="none" stroke="#fff" stroke-width="0.9"/>
            <polyline points="3,4 6,6.4 9,4" fill="none" stroke="#fff" stroke-width="0.9"/>
          </svg>
          <span>Derek@ridgemarkbuilding.com.au</span>
        </li>
        <li class="contact-item">
          <svg class="contact-icon" viewBox="0 0 12 12" aria-hidden="true">
            <circle cx="6" cy="6" r="6" fill="#4fd8cf"/>
            <rect x="4.2" y="2.6" width="3.6" height="6.8" rx="0.7" fill="none" stroke="#fff" stroke-width="0.9"/>
          </svg>
          <span>0400 215 397</span>
        </li>
        <li class="contact-item">
          <svg class="contact-icon" viewBox="0 0 12 12" aria-hidden="true">
            <circle cx="6" cy="6" r="6" fill="#4fd8cf"/>
            <path d="M6 9.6 C4.2 7.4 3.6 6.3 3.6 5.2 A2.4 2.4 0 0 1 8.4 5.2 C8.4 6.3 7.8 7.4 6 9.6 Z" fill="#fff"/>
            <circle cx="6" cy="5.2" r="0.9" fill="#4fd8cf"/>
          </svg>
          <span>14 Tarrington Loop<br>Halden Bay WA 6209</span>
        </li>
      </ul>
    </section>
  </main>
</body>
</html>
```